Bed & Breakfast Wordpress Theme - Design Only

We are looking for a Wordpress theme for an award winning UK Bed & Breakfast (Guesthouse) www.fernbrookinn.co.uk
You will see that the current site is basic and dated, we need a new site that showcases the very high standard of rooms on offer and is geared towards both mobile and desktop browsing.
We would like the colours that have been used in the rooms and building (as seen on the current website) to feature in the design.
We particularly like the look of this accommodation provider website: http://www.marlowdenbarns.co.uk
Selected website images can be downloaded here, feel free to use more from the existing website too:
https://www.filevaultly.com/s/qz81mv4rt7kw0pn/website%20images.zip
Target Market(s)
The accommodation is upmarket and the design needs to subtly communicate this.
The accommodation attracts a varied mix of ages so needs to be up scale without being overly modern.
Industry/Entity Type
Accommodation
Requirements
Must have
- As the accommodation does not have a logo we need a basic typographic logo incorporated into the design.
Colours of the building and rooms must be integrated into the design in some way.
A bold homepage that allows images of the rooms on offer and key information to be visibale above the fold. The goal of the homepage is for someone to then click Rooms or Prices so calls to action may help here.
Separate designs for a sidebar and full width version of sub pages.
An area that shows off the awards won by the company on all pages and space for testimonials.
The site must enable an easy transition from - homepage - to rooms - to prices with possible call to action buttons in the top right corner on these pages
The site needs to have a Homepage layout, a general sub page layout, and a 'Rooms' page layout which will showcase all rooms available possibly in a grid layout.
Nice to have
- Please use some of the images available currently on the website in your mockup, particularly of the building and rooms.
Should not have
- No need for any type of booking fields or engine as the booking system will be embedded on a full width page.

```html
<!DOCTYPE html>
<html lang="en">
<head>
<meta charset="utf-8">
<title>The Fernbrook Inn – Forest B&amp;B</title>
<link rel="stylesheet" href="https://fonts.googleapis.com/css2?family=Lora:ital,wght@0,400;0,700;1,400&family=Open+Sans:wght@400;600&display=swap">
<style>
:root{
  --page-bg:#ece5d4;
  --panel:#ffffff;
  --ink:#1e1a1a;
  --muted:#6f6868;
  --plum:#4a3438;
  --mauve:#9a8a8e;
  --rule:#e2dcd6;
  --gold:#e4cf6e;
  --gold-dark:#c9b04c;
  --chevron:#c9a9a0;
}
*{box-sizing:border-box;margin:0;padding:0}
html,body{width:1200px;height:900px;overflow:hidden}
body{
  background:radial-gradient(ellipse at 50% 30%,#f3eee1 0%,var(--page-bg) 70%,#e3dac6 100%);
  font-family:"Open Sans",Arial,sans-serif;color:var(--ink);position:relative;
}
.site-header{position:absolute;left:0;top:0;width:1200px;height:120px}
.brand{position:absolute;left:118px;top:36px}
.brand-name{font-family:"Lora",Georgia,serif;font-size:38px;font-weight:400;color:var(--ink);line-height:1;letter-spacing:-.3px}
.brand-tagline{margin-top:14px;font-size:11px;letter-spacing:4.6px;color:#7a7470;text-transform:uppercase}
.availability{position:absolute;left:742px;top:50px;font-family:"Lora",Georgia,serif}
.availability small{display:block;font-size:12px;color:#3a3434}
.availability a{display:block;margin-top:4px;font-size:17px;color:var(--ink);text-decoration:none;letter-spacing:.3px}
.header-divider{position:absolute;left:880px;top:45px;width:1px;height:47px;background:#bdb5ab}
.contact-list{position:absolute;left:908px;top:40px;list-style:none}
.contact-list li{display:flex;align-items:center}
.contact-list .phone{font-family:"Lora",Georgia,serif;font-size:21px;letter-spacing:.8px}
.contact-list .email{margin-top:6px;font-family:"Lora",Georgia,serif;font-size:12px}
.contact-list svg{width:16px;height:16px;margin-right:14px;fill:var(--ink)}

.main-nav{position:absolute;left:91px;top:127px;width:1018px;height:60px;background:var(--panel);
  border:1px solid #ddd6c8;box-shadow:0 8px 8px -6px rgba(80,60,40,.35)}
.main-nav ul{list-style:none;display:flex;height:100%}
.main-nav li{position:relative;display:flex;align-items:center;justify-content:center;font-size:14px;color:var(--ink);border-right:1px solid #ece8e2}
.main-nav li:nth-child(6){border-right:none}
.main-nav .chev{width:9px;height:6px;margin-left:10px;fill:none;stroke:var(--chevron);stroke-width:1.6}
.book-btn{position:absolute;left:850px;top:9px;width:133px;height:41px;background:linear-gradient(#ecd97f,var(--gold));
  border:1px solid var(--gold-dark);border-radius:3px;display:flex;align-items:center;justify-content:center;
  font-size:12px;letter-spacing:2.4px;color:#3a3220}

.content-panel{position:absolute;left:91px;top:206px;width:1018px;height:720px;background:var(--panel);border:1px solid #ddd6c8}
.hero{position:absolute;left:33px;top:33px;width:950px;height:426px;overflow:hidden;
  background:
    radial-gradient(ellipse at 20% 60%,rgba(214,150,150,.55),transparent 45%),
    radial-gradient(ellipse at 75% 75%,rgba(170,190,180,.6),transparent 40%),
    radial-gradient(ellipse at 60% 30%,rgba(240,235,225,.9),transparent 50%),
    linear-gradient(135deg,#b89676 0%,#d9c3a6 40%,#e8dac6 60%,#b9926a 100%);
  box-shadow:0 10px 14px -8px rgba(0,0,0,.2)}
.hero-photo{position:absolute;inset:0}
.hero-copy{position:absolute;left:0;right:0;top:108px;text-align:center;font-family:"Lora",Georgia,serif;color:var(--plum)}
.hero-copy p{font-size:17px;color:#4f3d3f}
.hero-copy h1{margin-top:4px;font-weight:400;font-size:49px;line-height:1.1;color:#3c2a2e}
.hero-copy h1 em{font-style:italic}
.learn-more{display:inline-block;margin-top:18px;width:156px;height:34px;line-height:34px;background:#4a3438;color:#f2ece8;
  border-radius:3px;font-family:"Open Sans",Arial,sans-serif;font-size:12px;letter-spacing:2.4px}
.slider-dots{position:absolute;left:440px;top:389px;display:flex;gap:7px}
.slider-dots span{width:11px;height:11px;border-radius:50%;background:rgba(120,110,110,.7)}
.slider-dots span.active{background:rgba(70,60,60,.85)}

.rule{position:absolute;left:33px;width:950px;height:1px;background:var(--rule)}
.intro{position:absolute;left:33px;top:500px;width:950px}
.intro-title{position:absolute;left:0;width:232px;text-align:center;top:14px;font-family:"Lora",Georgia,serif;font-weight:400;
  font-size:35px;line-height:38px;color:var(--mauve)}
.intro-text{position:absolute;left:264px;top:30px;width:680px;font-size:15px;line-height:32px;color:var(--muted)}
</style>
</head>
<body>
<header class="site-header">
  <div class="brand">
    <div class="brand-name">The Fernbrook Inn</div>
    <div class="brand-tagline">Forest B&amp;B - Ashcombe</div>
  </div>
  <div class="availability">
    <small>For room availability</small>
    <a href="#">CONTACT US</a>
  </div>
  <div class="header-divider"></div>
  <ul class="contact-list">
    <li class="phone"><svg viewBox="0 0 24 24"><path d="M6.6 10.8a15.2 15.2 0 0 0 6.6 6.6l2.2-2.2c.3-.3.7-.4 1-.2 1.1.4 2.3.6 3.6.6.6 0 1 .4 1 1V20c0 .6-.4 1-1 1A17 17 0 0 1 3 4c0-.6.4-1 1-1h3.5c.6 0 1 .4 1 1 0 1.3.2 2.5.6 3.6.1.3 0 .7-.2 1z"/></svg>01632 960418</li>
    <li class="email"><svg viewBox="0 0 24 24"><path d="M2 6l10 7 10-7v12H2z M2 4h20l-10 7z"/></svg>enquiries@fernbrookinn.co.uk</li>
  </ul>
</header>

<nav class="main-nav">
  <ul>
    <li style="width:125px">Home</li>
    <li style="width:140px">About Us</li>
    <li style="width:141px">Gallery</li>
    <li style="width:145px">Rooms<svg class="chev" viewBox="0 0 10 6"><path d="M1 1l4 4 4-4"/></svg></li>
    <li style="width:141px">Prices<svg class="chev" viewBox="0 0 10 6"><path d="M1 1l4 4 4-4"/></svg></li>
    <li style="width:150px">Location</li>
  </ul>
  <a class="book-btn">BOOK ONLINE</a>
</nav>

<main class="content-panel">
  <section class="hero">
    <div class="hero-photo" role="img" aria-label="Breakfast table laid with teacups, glasses and a menu in the guesthouse dining room"></div>
    <div class="hero-copy">
      <p>We are delighted to offer a range of</p>
      <h1><em>locally sourced</em> breakfast</h1>
      <a class="learn-more">LEARN MORE</a>
    </div>
    <div class="slider-dots"><span></span><span></span><span class="active"></span><span></span></div>
  </section>

  <div class="rule" style="top:484px"></div>
  <section class="intro">
    <h2 class="intro-title">small<br>&amp; friendly<br>hotel</h2>
    <p class="intro-text">The Fernbrook Inn Forest B&amp;B in Ashcombe is situated in the heart of the Forest Village of Ashcombe. Ponies and cattle can wander freely throught the village. Watch out for them in the village the ponies have been known to wander into Grangers.</p>
  </section>
  <div class="rule" style="top:663px"></div>
</main>
</body>
</html>
```